Brightpaw Website

website will need to have the following features:
• Photo Galleries of each species (Dogs, Cats, Birds, Fish, Reptiles, Rabbits) in a light box popup
o Each species may have several different categories for example:
 Fish
• Marine fish
• Fresh water
• tropical
• Cichlid
• Information Fact sheets of each species – Downloaded as a pdf which can be either
o Care Sheets
o Training Sheets
• Members Area
o Username (Email Address) & Password login
o New signups
o Exclusive Member Deals
o Newsletter options

The front page must be very simple (for example lumavale.com.au) contain the following:
• Product of the week - which can be purchased online
o Short details
o Cost
• Pet Club Sign up picture
• Animal of the week/month
• Contact Phone Number and addresses of the stores
• A jQuery slideshow (Images could include stores, pets etc…)
The main page MUST keep simple. We do not want it cluttered.

Inner Page
The animals / reptile page will need to have:
• Short description of the species
• Photo Galleries
• A list of what is in stock and the list needs to clearly be sorted by each store (Use of Tabs maybe).
• Facts sheets / Info sheets
The type of website ideas (not the type of look that we are necessary after) is and the sort of content that we want to offer are as follows:

http://www.scalenook.com.au/
http://www.marrowdenpets.com.au/
http://www.thefurloft.com.au
http://www.critterhaven.net.au

Colour in the new website:
Blue
Red
Grey
Yellow

Original site:

http://www.pawglint.com.au
Updates

Hi Guys,

We had feedback from the client and they would like to see a few dark designs.

Thanks                                   

Reason: We would like to reopen this contest back up for a further week

Target Market(s)

Targeting animal lovers

Industry/Entity Type

Store

Requirements
Should not have
• Alter the logo in anyway

```html
<!DOCTYPE html>
<html lang="en">
<head>
<meta charset="utf-8">
<title>Brightpaw</title>
<link href="https://fonts.googleapis.com/css2?family=Jost:wght@400;500&family=Noto+Sans:ital,wght@0,400;1,700&display=swap" rel="stylesheet">
<style>
:root{
  --backdrop:#e2e2e2;
  --backdrop-band:#e8e8e8;
  --page:#ffffff;
  --brand-blue:#1a9ae0;
  --link-blue:#1a8fd6;
  --heading-red:#d8141c;
  --body-text:#555555;
  --rule:#e3e3e3;
  --panel:#d2d2d2;
  --field:#f7f7f7;
  --button-top:#4aa8e8;
  --button-bottom:#1663b0;
}
*{box-sizing:border-box;margin:0;padding:0}
html,body{width:1200px;height:687px;overflow:hidden}
body{
  position:relative;
  background:linear-gradient(to bottom,var(--backdrop) 0,var(--backdrop) 82px,var(--backdrop-band) 82px,var(--backdrop-band) 230px,var(--backdrop) 230px);
  font-family:"Noto Sans",Verdana,sans-serif;
}
.page{position:absolute;left:176px;top:122px;width:851px;height:565px;background:var(--page)}
.page > *{position:absolute}
.brand{left:30px;top:28px;font-family:"Jost",sans-serif;font-weight:500;font-size:34px;color:var(--brand-blue);letter-spacing:-0.5px}
.account{right:50px;top:31px;text-align:right;font-size:10.5px;color:var(--body-text);line-height:18px}
.account a{color:var(--link-blue);font-style:italic;font-weight:700;text-decoration:none}
.social-square{display:inline-block;width:23px;height:23px;border-radius:3px;background:#5b78b4;vertical-align:middle;margin-left:3px}
.main-nav{left:16px;top:145px;width:92px;text-align:center;font-family:"Jost",sans-serif;font-size:12px}
.main-nav a{display:block;color:var(--link-blue);text-decoration:none;height:33.5px;line-height:14px;padding-top:0}
.main-nav a + a{border-top:1px solid transparent}
.nav-rule{display:block;width:50px;height:1px;margin:-10px auto 9px;background:linear-gradient(to right,transparent,#c9c9c9,transparent)}
.divider{width:1px;background:var(--rule)}
.divider.side{left:131px;top:121px;height:408px}
.divider.intro{left:592px;top:128px;height:160px}
.signup{left:21px;top:312px;width:95px;height:231px;background:var(--panel);border-radius:7px;padding:10px;font-size:9px;color:#222}
.signup h2{font-weight:400;font-size:10.5px;color:var(--link-blue);margin:3px 0 17px}
.signup label{display:block;line-height:11px}
.signup .field{display:block;width:74px;height:12px;background:var(--field);border-radius:2px;box-shadow:inset 0 1px 2px rgba(0,0,0,.15);margin:2px 0 13px}
.signup .submit{position:absolute;left:17px;top:189px;width:61px;height:27px;border-radius:5px;background:linear-gradient(var(--button-top),var(--button-bottom));color:#fff;font-size:12px;font-weight:700;display:flex;align-items:center;justify-content:center;gap:4px;box-shadow:0 1px 2px rgba(0,0,0,.3)}
.slideshow{left:149px;top:121px;width:429px;height:171px;border-radius:6px;overflow:hidden;background:linear-gradient(100deg,#3b5f6a 0%,#a27a4e 18%,#111 38%,#1a1a1a 58%,#8a6c5c 75%,#3a3a3a 100%);box-shadow:0 2px 4px rgba(0,0,0,.3)}
.slideshow svg{position:absolute;top:78px}
.intro-text{left:606px;top:126px;width:230px;font-size:12px;line-height:17.3px;color:var(--body-text)}
.section-title{font-family:"Jost",sans-serif;font-size:14px;color:var(--heading-red);font-weight:400}
.gallery-title{left:148px;top:306px}
.contact-title{left:148px;top:431px}
.thumb{top:336px;width:96px;height:76px;box-shadow:1px 2px 4px rgba(0,0,0,.35)}
.thumb.fish{left:180px;background:linear-gradient(135deg,#6a8aa0,#2c4fb8 55%,#8a7a5a)}
.thumb.kitten{left:298px;background:radial-gradient(circle at 50% 60%,#e0a060,#f1f1ef 75%)}
.thumb.snake{left:416px;background:linear-gradient(160deg,#2a4a22,#56a832 55%,#1e3a1a)}
.thumb.tortoise{left:534px;background:radial-gradient(circle at 50% 55%,#8a6a3a,#2a2418 70%,#111)}
.thumb.puppy{left:648px;background:radial-gradient(circle at 45% 50%,#e2c2a0,#c8184a 65%)}
.contact-block{top:479px;font-size:12.3px;line-height:17px;color:var(--link-blue)}
.contact-block.first{left:180px}
.contact-block.second{left:404px}
.contact-block.third{left:630px;width:185px}
</style>
</head>
<body>
<div class="page">
  <div class="brand">Brightpaw</div>

  <div class="account">
    <a href="#">Log in</a> or <a href="#">Sign up</a> here<br>
    find us on <span class="social-square" aria-hidden="true"></span>
  </div>

  <nav class="main-nav">
    <a href="#">Photo Gallery</a><span class="nav-rule"></span>
    <a href="#">Pets</a><span class="nav-rule"></span>
    <a href="#">Membership</a><span class="nav-rule"></span>
    <a href="#">Newsletter</a>
  </nav>

  <div class="divider side"></div>

  <form class="signup">
    <h2>Sign up</h2>
    <label>Name</label><span class="field"></span>
    <label>Surname</label><span class="field"></span>
    <label>Email</label><span class="field"></span>
    <label>Password</label><span class="field"></span>
    <span class="submit">Sign Up
      <svg width="6" height="8" viewBox="0 0 6 8"><path d="M0 0L6 4L0 8Z" fill="#fff"/></svg>
    </span>
  </form>

  <div class="slideshow" role="img" aria-label="Slideshow photo of a coral reef aquarium with colourful tropical fish">
    <svg style="left:8px" width="10" height="18" viewBox="0 0 10 18"><path d="M10 0L0 9L10 18Z" fill="#fff"/></svg>
    <svg style="right:8px" width="10" height="18" viewBox="0 0 10 18"><path d="M0 0L10 9L0 18Z" fill="#fff"/></svg>
  </div>

  <div class="divider intro"></div>

  <p class="intro-text">Lorem ipsum dolor sit amet, con-<br>sectetuer adipiscing elit, sed diam<br>nonummy nibh euismod tincidunt<br>ut laoreet dolore magna aliquam<br>erat volutpat. Ut wisi enim ad<br>minim veniam, quis nostrud exerci<br>tation ullamcorper suscipit lobortis<br>nisl ut aliquip ex ea commodo con-<br>sequat. Duis autem vel eum iriure<br>dolor in hendrerit in vulputate velit</p>

  <h2 class="section-title gallery-title">Photo Gallery</h2>
  <div class="thumb fish" role="img" aria-label="Photo of a blue striped tropical fish"></div>
  <div class="thumb kitten" role="img" aria-label="Photo of a ginger kitten"></div>
  <div class="thumb snake" role="img" aria-label="Photo of a green snake on a branch"></div>
  <div class="thumb tortoise" role="img" aria-label="Photo of a tortoise"></div>
  <div class="thumb puppy" role="img" aria-label="Photo of a pug puppy on a pink blanket"></div>

  <h2 class="section-title contact-title">Contact us</h2>
  <address class="contact-block first" style="font-style:normal">224 Lorem ipsum dolor<br>Loremeiem igfiapsum dolor 4122<br>Lorem ipsum dolorl 1800 555 170<br>Or +61 (0)7 3012 4478</address>
  <address class="contact-block second" style="font-style:normal">224 Lorem ipsum dolor<br>Loremeiem igfiapsum dolor 4122<br>Lorem ipsum dolorl 1800 555 170<br>Or +61 (0)7 3012 4478</address>
  <address class="contact-block third" style="font-style:normal">224 Lorem ipsum dolor<br>Loremeiem igfiapsum dolor<br>4122<br>Lorem ipsum dolorl 1800 555</address>
</div>
</body>
</html>
```